Business card design needed

The company name is Pellwick Architects. We are an architectural company based in Melbourne,Australia that has a mix of client base from health care, commercial office, aged care, multi-residential, single residential and retail. Design type is contemporary.

Suggest the base colours need to be black and white. Please leave an area on the back of the card available for handwritten notes.

Target Market(s)

Generally corporate, aged 30 to 65

Industry/Entity Type

Residential

Contact Information for Business Card

Pellwick Architects
Dane Pellwick
7 Horbury Street
Northvale VIC 3059
T (03) 9572 4016
M 0431 607 295
E dp@pellwickarc.com.au

Logo Text

PA

Logo styles of interest
Emblem Logo
Abstract Logo
Lettermark Logo
Requirements
Must have
• I am having trouble attaching a sketch so would really appreciate your effort to try the following brief.

Black and White (B&W)
Would like different card cutout profile. Logo Example, use the half circle curve of the G to form the left edge of the card with no margin. The A is to sit inside the G, connected to the G by its horizontal. The A has its cross bar and lower right leg removed. Card in black, text in white.

Back of card to be black text on white background with services provided.

Client Focused Service
Architecture and Design
Functional Planning
Town Planning
Feasability Studies
Contract Documentation
Contract Administration
Project Management

Simple elegant text, Ariel or similar
Nice to have
• Integrated logo and card cut-out.

Card base black on front, white on back
Should not have
• Too many colours
Fussy details

```html
<!DOCTYPE html>
<html lang="en">
<head>
<meta charset="utf-8">
<title>Pellwick Architects — Business Card</title>
<link rel="stylesheet" href="https://fonts.googleapis.com/css2?family=Jost:wght@200;300&display=swap">
<style>
  :root {
    --card-black: #000000;
    --photo-dark: #2c2c2c;
    --photo-mid: #3a3a3a;
    --photo-light: #474747;
    --ink-white: #ffffff;
    --ink-soft: #ececec;
  }
  html, body {
    margin: 0;
    padding: 0;
    width: 1200px;
    height: 665px;
    overflow: hidden;
    background: var(--card-black);
  }
  .card {
    position: relative;
    width: 1200px;
    height: 665px;
    background: var(--card-black);
    overflow: hidden;
    font-family: "Jost", "Helvetica Neue", Arial, sans-serif;
    color: var(--ink-white);
  }
  .card__solid {
    position: absolute;
    left: 0;
    top: 0;
    width: 497px;
    height: 665px;
    background: var(--card-black);
  }
  .card__plans {
    position: absolute;
    left: 497px;
    top: 0;
    width: 703px;
    height: 665px;
    background:
      radial-gradient(ellipse at 55% 15%, var(--photo-light) 0%, transparent 45%),
      linear-gradient(160deg, var(--photo-mid) 0%, var(--photo-dark) 60%, #262626 100%);
  }
  .lettermark {
    position: absolute;
    left: 22px;
    top: 345px;
    margin: 0;
    font-weight: 200;
    font-size: 230px;
    line-height: 1;
    letter-spacing: 0.02em;
    color: var(--ink-white);
    white-space: nowrap;
  }
  .wordmark {
    position: absolute;
    top: 246px;
    margin: 0;
    font-weight: 200;
    font-size: 94px;
    line-height: 1;
    color: var(--ink-white);
    white-space: nowrap;
  }
  .wordmark--first {
    right: 736px;
    letter-spacing: 0.08em;
  }
  .wordmark--second {
    left: 525px;
    letter-spacing: 0.15em;
  }
  .contact {
    position: absolute;
    left: 497px;
    width: 692px;
    top: 526px;
    margin: 0;
    text-align: center;
    font-style: normal;
    font-weight: 300;
    font-size: 28px;
    line-height: 42px;
    color: var(--ink-soft);
  }
  .contact__line {
    display: block;
    white-space: nowrap;
  }
</style>
</head>
<body>
  <main class="card">
    <div class="card__solid"></div>
    <div class="card__plans" role="img" aria-label="Darkened photograph of rolled architectural plans lying on drafting sheets"></div>

    <div class="lettermark" aria-label="PA lettermark">PA</div>

    <h1 class="wordmark wordmark--first">PELLWICK</h1>
    <p class="wordmark wordmark--second">ARCHITECTS</p>

    <address class="contact">
      <span class="contact__line">Dane Pellwick 7 Horbury Street Northvale VIC 3059</span>
      <span class="contact__line">Tel (03) 9572 4016 M 0431 607 295</span>
      <span class="contact__line">Email: dp@pellwickarc.com.au</span>
    </address>
  </main>
</body>
</html>
```